HALT THE CLAIMS

I'm virtually ready to launch my site, but I have a number of edits and modifications that need to be implemented. More importantly, I'm always looking to improve my site, particularly now that I am making my proverbial "FIRST IMPRESSION." Thus, I'm willing to see if there is someone who can add creativity and perhaps improve what I already have, particularly on the All Important Front Page.

Need extra days to review

```html
<!DOCTYPE html>
<html lang="en">
<head>
<meta charset="utf-8">
<title>Halt The Claims</title>
<link rel="stylesheet" href="https://fonts.googleapis.com/css2?family=Roboto:wght@400;500;700;900&family=Tinos&display=swap">
<style>
:root{
  --red:#a50014;
  --red-bright:#b3071c;
  --navy:#0c1a3e;
  --navy-deep:#16224a;
  --blue-text:#1d3f8f;
  --ink:#333;
  --grey:#8a8a8a;
  --dark:#161616;
  --white:#fff;
}
*{box-sizing:border-box;margin:0;padding:0}
html,body{width:1200px;height:4367px;overflow:hidden}
body{position:relative;background:var(--white);font-family:"Roboto",sans-serif;color:var(--ink)}
.red{color:var(--red)}
.btn{position:absolute;display:flex;align-items:center;justify-content:center;gap:10px;height:40px;border-radius:20px;font:700 14px "Roboto",sans-serif;color:#fff;background:var(--red);text-transform:uppercase;letter-spacing:.2px}
.btn svg{width:14px;height:14px}
.btn.navy{background:var(--navy)}
.btn.light{background:#fff;color:var(--red)}
.section-title{position:absolute;left:0;width:1200px;text-align:center;font:900 34px "Roboto",sans-serif;color:var(--navy);letter-spacing:.3px}
.section-title::after{content:"";display:block;width:56px;height:4px;background:var(--red);margin:10px auto 0}

/* header */
.site-nav{position:absolute;top:0;left:0;width:1200px;height:95px;background:#fff}
.site-nav a{position:absolute;top:40px;font:400 15px "Roboto",sans-serif;color:#333;text-decoration:none}
.site-nav .sep{position:absolute;top:40px;font-size:15px;color:#333}
.brand{position:absolute;left:508px;top:8px;width:184px;height:120px;z-index:3;display:flex;flex-direction:column;align-items:center;justify-content:center;gap:6px;background:#fff;border-radius:0 0 90px 90px}
.brand-dot{width:34px;height:34px;border-radius:50%;background:var(--red)}
.brand-name{font:900 18px "Roboto",sans-serif;color:var(--navy);text-align:center;line-height:1.1}

/* hero */
.hero{position:absolute;top:95px;left:0;width:1200px;height:638px;background:linear-gradient(160deg,#5a3b22 0%,#3a2616 40%,#1c140d 75%,#0f0b08 100%)}
.hero-title{position:absolute;top:250px;width:1200px;text-align:center;font:900 64px "Roboto",sans-serif;color:#fff;letter-spacing:1px;text-shadow:0 3px 8px rgba(0,0,0,.5)}

/* about */
.about-lead{position:absolute;top:884px;left:172px;width:856px;text-align:center;font-size:15px;line-height:26px}
.about-plan{position:absolute;top:952px;width:1200px;text-align:center;font-size:14.5px;color:var(--blue-text)}
.img-fill{position:absolute}
.about-copy{position:absolute;left:629px;top:1022px;width:460px;font-size:15px;line-height:28.3px;text-align:justify;color:#444}
.about-copy p{margin-bottom:9px}
.quote{position:absolute;left:113px;top:1552px;font:16px "Tinos",serif;line-height:30px;color:var(--navy)}
.dots{position:absolute;background-image:radial-gradient(var(--red) 1.2px,transparent 1.4px);background-size:9px 9px}

/* owners */
.owners-photo{position:absolute;left:0;top:1744px;width:592px;height:524px;background:linear-gradient(135deg,#4a3a2a,#2a2420 55%,#6b6460)}
.owners-panel{position:absolute;left:581px;top:1793px;width:619px;height:526px;background:var(--red)}
.owners-bar{position:absolute;left:592px;top:1851px;width:22px;height:410px;background:var(--navy)}
.owners-title{position:absolute;left:668px;top:1858px;font:900 34px "Roboto",sans-serif;color:#fff}
.owners-title::after{content:"";display:block;width:56px;height:4px;background:#fff;margin-top:8px}
.owners-copy{position:absolute;left:668px;top:1924px;width:468px;font-size:15px;line-height:27.5px;color:#fff;text-align:justify}

/* services */
.services-lead{position:absolute;top:2462px;width:1200px;text-align:center;font-size:15px;line-height:26px}
.service-card{position:absolute;width:474px;height:164px;background:#fff;border-radius:82px;box-shadow:0 4px 18px rgba(0,0,0,.12)}
.service-card .thumb{position:absolute;left:8px;top:12px;width:140px;height:140px;border-radius:50%}
.service-card h3{position:absolute;left:166px;top:22px;font:500 15px "Roboto",sans-serif;color:#222;text-transform:uppercase}
.service-card p{position:absolute;left:166px;top:48px;width:280px;font-size:13px;line-height:25.5px;color:var(--grey)}
.service-card .more{position:absolute;left:166px;top:124px;font:700 14px "Roboto",sans-serif;color:var(--red);display:flex;gap:7px;align-items:center}
.more svg{width:13px;height:13px}

/* faq */
.faq{position:absolute;top:3082px;left:0;width:1200px;height:591px;background:linear-gradient(180deg,#1c2850,#16213f)}
.faq .section-title{color:#fff;top:114px}
.faq-item{position:absolute;left:110px;width:478px;height:51px;background:#fff;border-radius:26px;display:flex;align-items:center;justify-content:space-between;padding:0 20px 0 30px;font-size:13.5px;color:#333}
.faq-item i,.faq-open i{width:11px;height:11px;border-radius:50%;background:var(--red);position:relative;flex:none}
.faq-item i::after,.faq-open i::after{content:"";position:absolute;left:3px;top:5px;width:5px;height:1.5px;background:#fff}
.faq-open{position:absolute;left:614px;top:3294px;width:476px;height:277px;background:#fff;border-radius:24px;overflow:hidden}
.faq-open .q{background:#f8e8ea;padding:14px 20px 12px 30px;display:flex;justify-content:space-between;align-items:center;font-size:13.5px;line-height:23px;color:#333}
.faq-open .a{padding:18px 22px 0 33px;font-size:13.5px;line-height:25.5px;color:var(--grey);text-align:justify}

/* contact */
.contact{position:absolute;top:3673px;left:0;width:1200px;height:632px;background:var(--dark)}
.c-icon{position:absolute;width:76px;height:76px;border-radius:50%;background:var(--red-bright);display:flex;align-items:center;justify-content:center}
.c-icon svg{width:30px;height:30px;fill:#fff}
.c-label{position:absolute;width:320px;text-align:center;color:#fff;font:700 17px "Roboto",sans-serif}
.c-value{position:absolute;width:320px;text-align:center;color:#fff;font-size:14px;line-height:26px}
.field{position:absolute;border:1.5px solid #d8d8d8;border-radius:26px;color:#fff;font-size:13px;padding-left:28px;display:flex;align-items:center}
.field.area{align-items:flex-start;padding-top:22px;border-radius:20px}

/* footer */
.site-footer{position:absolute;top:4305px;left:0;width:1200px;height:62px;background:var(--red)}
.site-footer .copy{position:absolute;left:112px;top:22px;color:#fff;font-size:14.5px}
.social{position:absolute;top:14px;width:34px;height:34px;border:1.5px solid #fff;border-radius:50%}
</style>
</head>
<body>

<header class="site-nav">
  <a style="left:207px">HOME</a><span class="sep" style="left:272px">|</span>
  <a style="left:300px">ABOUT</a><span class="sep" style="left:372px">|</span>
  <a style="left:400px">SERVICES</a>
  <a style="left:708px">FAQ</a><span class="sep" style="left:757px">|</span>
  <a style="left:785px">CONTACT US</a><span class="sep" style="left:899px">|</span>
  <a style="left:926px">LOGIN
    <svg width="13" height="13" viewBox="0 0 14 14" fill="none" stroke="#333" stroke-width="1.3" style="vertical-align:-1px"><circle cx="7" cy="4.5" r="3"/><path d="M1.5 13c0-3 2.5-5 5.5-5s5.5 2 5.5 5z"/></svg></a>
  <div class="brand"><span class="brand-dot"></span><span class="brand-name">Halt The<br>Claims</span></div>
</header>

<section class="hero" role="img" aria-label="Courtroom scene with an attorney addressing a jury in a wood-panelled room">
  <h1 class="hero-title">HALT THE CLAIMS</h1>
  <span class="btn" style="left:515px;top:352px;width:170px">GET STARTED
    <svg viewBox="0 0 14 14"><circle cx="7" cy="7" r="7" fill="#fff"/><path d="M5 4l3.5 3L5 10" stroke="#a50014" stroke-width="1.8" fill="none"/></svg></span>
</section>

<section class="about">
  <h2 class="section-title" style="top:812px">ABOUT US</h2>
  <p class="about-lead"><span class="red">HTC</span> is a group of attorney and legal assistants with many years of experience in litigation, who are devoted to <span class="red">PREVENTING LEGAL CLAIMS</span> and <span class="red">COSTLY LAWSUITS</span> through a variety of <span class="red">FREE</span> and <span class="red">VERY AFFORDABLE</span> services described below.</p>
  <p class="about-plan">OUR UNIQUE SERVICE PLAN MAKES IT POSSIBLE FOR US TO HALT THE CLAIMS.</p>

  <div class="img-fill" style="left:145px;top:1060px;width:320px;height:320px;background:#eceaf8"></div>
  <div class="dots" style="left:466px;top:1150px;width:46px;height:55px"></div>
  <div class="dots" style="left:196px;top:1380px;width:60px;height:48px"></div>
  <div class="img-fill" role="img" aria-label="Banknote portrait wearing a face mask" style="left:117px;top:1024px;width:322px;height:329px;background:linear-gradient(135deg,#bdbcb0,#7c7d73 60%,#9aa08f)"></div>
  <div class="img-fill" role="img" aria-label="Hand signing a document beside scales of justice" style="left:258px;top:1208px;width:306px;height:324px;background:linear-gradient(160deg,#3a3530,#181512 50%,#d8d4cc)"></div>

  <div class="about-copy">
    <p>A homebuilding company was sued by a former employee who claimed to have been promised a more favorable sales area, which claim was disputed by the homebuilder. There was no evidence that such a promise had been made, other than the plaintiff’s oral testimony. The company had the case dismissed, but spent $10,000 defending the case.</p>
    <p>And even though it was awarded its attorney’s fees, the plaintiff proved uncollectible. Had the company been an HTC member, the case likely would never have been filed. Call for your <span class="red">FREE CONSULTATION</span> and let us show you why the plaintiff likely would not have found a contingency attorney (as was the case) or been able to pay an attorney on an hourly basis. In short, by using HTC’s services, the plaintiff’s claim would not have been filed.</p>
    <p>In our vast experience with commercial litigation, we believe that a very large percentage of litigation cases hinge on “he said / she said” issues. By using HTC’s services, we believe we can INSULATE you and your business from all such issues, which will <span class="red">MINIMIZE</span> your <span class="red">EXPOSURE</span> to <span class="red">LEGAL CLAIMS</span> and <span class="red">LAWSUITS</span>.</p>
  </div>
  <p class="quote">An OUNCE of PREVENTION is worth a POUND of CURE.<br><span class="red">Elias Whitcombe.</span></p>
  <span class="btn" style="left:361px;top:1619px;width:169px">CONTACT US
    <svg viewBox="0 0 14 14"><circle cx="7" cy="7" r="7" fill="#fff"/><path d="M5 4l3.5 3L5 10" stroke="#a50014" stroke-width="1.8" fill="none"/></svg></span>
  <span class="btn navy" style="left:541px;top:1619px;width:298px">SCHEDULE FREE CONSULTATION
    <svg viewBox="0 0 14 14"><circle cx="7" cy="7" r="7" fill="#fff"/><path d="M5 4l3.5 3L5 10" stroke="#0c1a3e" stroke-width="1.8" fill="none"/></svg></span>
</section>

<section class="owners">
  <div class="owners-photo" role="img" aria-label="Businessman in a suit writing at a desk in a library"></div>
  <div class="owners-panel"></div>
  <div class="owners-bar"></div>
  <h2 class="owners-title">BUSINESS OWNERS</h2>
  <p class="owners-copy">Halt The Claims (HTC) Is An Extremely Affordable Legal Service Plan (As Little As $8.00 Per Month) That INSULATES Business Owners From Unwarranted LEGAL CLAIMS And Expensive LAWSUITS. Our Plan Uses Local, Experienced, Quality Attorneys Who Focus On PROBLEM PREVENTION Using Proprietary Tools Available Only To HTC Members. Contact Us For A Free Consultation And Receive A FREE OVERVIEW Of Your Business To See If You Are Truly Insulated From Legal Claims.<br><span style="display:block;margin-top:9px;text-align:left">Contact Us To Find Out How You Can Join Us To Halt The Claims!!</span></p>
  <span class="btn light" style="left:668px;top:2206px;width:292px">SCHEDULE FREE CONSULTATION
    <svg viewBox="0 0 14 14"><circle cx="7" cy="7" r="7" fill="#a50014"/><path d="M5 4l3.5 3L5 10" stroke="#fff" stroke-width="1.8" fill="none"/></svg></span>
  <span class="btn navy" style="left:966px;top:2206px;width:170px">LEARN MORE
    <svg viewBox="0 0 14 14"><circle cx="7" cy="7" r="7" fill="#fff"/><path d="M5 4l3.5 3L5 10" stroke="#0c1a3e" stroke-width="1.8" fill="none"/></svg></span>
</section>

<section class="services">
  <h2 class="section-title" style="top:2394px">OUR SERVICES</h2>
  <p class="services-lead">The price for a membership is a ridiculously low $9.95 PER WEEK. We believe that this fee is very affordable.<br>So what is it? Membership includes the following:</p>

  <article class="service-card" style="left:112px;top:2549px">
    <div class="thumb" role="img" aria-label="Hands reviewing paperwork on a desk" style="background:linear-gradient(135deg,#d9c08a,#7d6a4e)"></div>
    <h3>FREE INITIAL CONSULTATION</h3>
    <p>As a prospective Halt The Claims (“HTC”) member, we urge you to schedule an initial consultation with us – at no charge</p>
    <span class="more">Read More <svg viewBox="0 0 14 14"><circle cx="7" cy="7" r="7" fill="#a50014"/><path d="M5 4l3.5 3L5 10" stroke="#fff" stroke-width="1.8" fill="none"/></svg></span>
  </article>
  <article class="service-card" style="left:614px;top:2549px">
    <div class="thumb" role="img" aria-label="Judge's gavel and scales on a desk" style="background:linear-gradient(135deg,#6b4a30,#1e1510)"></div>
    <h3>PROPRIETARY CONTRACT LANGUAGE</h3>
    <p>HTC members are entitled to incorporate exclusive proprietary contract language in their contracts, work orders, and other</p>
    <span class="more">Read More <svg viewBox="0 0 14 14"><circle cx="7" cy="7" r="7" fill="#a50014"/><path d="M5 4l3.5 3L5 10" stroke="#fff" stroke-width="1.8" fill="none"/></svg></span>
  </article>
  <article class="service-card" style="left:112px;top:2749px">
    <div class="thumb" role="img" aria-label="Stressed man reading a letter" style="background:linear-gradient(135deg,#b8b2aa,#6a5f58)"></div>
    <h3>FREE ATTORNEY LETTERS</h3>
    <p>In addition to free monthly consultations, HTC members can have their local HTC Attorney send out a letter regarding their</p>
    <span class="more">Read More <svg viewBox="0 0 14 14"><circle cx="7" cy="7" r="7" fill="#a50014"/><path d="M5 4l3.5 3L5 10" stroke="#fff" stroke-width="1.8" fill="none"/></svg></span>
  </article>
  <article class="service-card" style="left:614px;top:2749px">
    <div class="thumb" role="img" aria-label="Paper document being handed across a desk" style="background:linear-gradient(135deg,#2a3340,#c9ccd0 60%,#1c2028)"></div>
    <h3>COLLECTIONS</h3>
    <p>HTC members can have their HTC Attorney pursue collection claims on a contingency fee basis, provided the claim is based on a</p>
    <span class="more">Read More <svg viewBox="0 0 14 14"><circle cx="7" cy="7" r="7" fill="#a50014"/><path d="M5 4l3.5 3L5 10" stroke="#fff" stroke-width="1.8" fill="none"/></svg></span>
  </article>
  <span class="btn" style="left:515px;top:2955px;width:170px">VIEW MORE
    <svg viewBox="0 0 14 14"><circle cx="7" cy="7" r="7" fill="#fff"/><path d="M5 4l3.5 3L5 10" stroke="#a50014" stroke-width="1.8" fill="none"/></svg></span>
</section>

<section class="faq">
  <h2 class="section-title">FREQUENTLY ASKED QUESTIONS</h2>
</section>
<div class="faq-item" style="top:3294px">Why should I be concerned about legal claims? <i></i></div>
<div class="faq-item" style="top:3370px">What does an HTC membership cost? <i></i></div>
<div class="faq-item" style="top:3445px">Provide more details about the value of HTC’s contract language <i></i></div>
<div class="faq-item" style="top:3521px">What does an HTC membership cost? <i></i></div>
<div class="faq-open">
  <div class="q"><span>If I’m a contractor, for example, how can an HTC membership<br>minimize legal claims against my business?</span><i></i></div>
  <p class="a">Lorem ipsum dolor sit amet, consectetur adipiscing elit. Suspendisse varius enim in eros elementum tristique. Duis cursus, mi quis viverra ornare, eros dolor interdum nulla, ut commodo diam libero vitae erat. Aenean faucibus nibh et justo cursus id rutrum lorem imperdiet. Nunc ut sem vitae risusLorem ipsum dolor sit amet, consectetur adipiscing elit.</p>
</div>

<section class="contact">
  <div class="c-icon" style="left:209px;top:77px"><svg viewBox="0 0 24 24"><path d="M6.6 10.8a15 15 0 006.6 6.6l2.2-2.2c.3-.3.7-.4 1-.2 1.1.4 2.3.6 3.6.6.6 0 1 .4 1 1V20c0 .6-.4 1-1 1A17 17 0 013 4c0-.6.4-1 1-1h3.5c.6 0 1 .4 1 1 0 1.3.2 2.5.6 3.6.1.3 0 .7-.2 1z"/></svg></div>
  <div class="c-icon" style="left:550px;top:77px"><svg viewBox="0 0 24 24"><path d="M3 5h18v2l-9 6-9-6z"/><path d="M3 9l9 6 9-6v10H3z"/></svg></div>
  <div class="c-icon" style="left:879px;top:77px"><svg viewBox="0 0 24 24"><path d="M12 2a7 7 0 00-7 7c0 5 7 13 7 13s7-8 7-13a7 7 0 00-7-7zm0 9.5A2.5 2.5 0 1112 6.5a2.5 2.5 0 010 5z"/></svg></div>
  <p class="c-label" style="left:87px;top:172px">PHONE</p>
  <p class="c-value" style="left:87px;top:198px">(555) 010-0142</p>
  <p class="c-label" style="left:428px;top:172px">Email</p>
  <p class="c-value" style="left:428px;top:198px">info@halttheclaims.com</p>
  <p class="c-label" style="left:757px;top:172px">Address</p>
  <p class="c-value" style="left:757px;top:198px">4820 Juniper Ridge Rd., Suite 210<br>Larkspur Vale, Westmark 10450</p>

  <div class="field" style="left:208px;top:293px;width:394px;height:53px">Name</div>
  <div class="field" style="left:213px;top:363px;width:394px;height:52px">Email Address</div>
  <div class="field" style="left:213px;top:427px;width:394px;height:53px">Phone Number</div>
  <div class="field area" style="left:625px;top:291px;width:397px;height:189px">Message</div>
  <span class="btn" style="left:515px;top:520px;width:208px;height:52px;border-radius:26px;font-size:16px">SUBMIT NOW
    <svg viewBox="0 0 14 14"><circle cx="7" cy="7" r="7" fill="#fff"/><path d="M5 4l3.5 3L5 10" stroke="#a50014" stroke-width="1.8" fill="none"/></svg></span>
</section>

<footer class="site-footer">
  <p class="copy">Copyright© 2023 Halttheclaims.net | All Rights Reserved</p>
  <span class="social" style="left:967px"></span>
  <span class="social" style="left:1011px"></span>
  <span class="social" style="left:1055px"></span>
</footer>

</body>
</html>
```